Trading Company needs a business card design, letter head design and email signature

We need a double-sided business card design, letter head design and an email signature. We have a logo design.

Possible Tag Lines:
• “Connecting Worlds, Building Excellence.”
• “Global Sourcing, Local Excellence.”
• “Bridging Borders, Building Quality.”
• “Worldwide Partnerships, Superior Goods.”
• “Where Quality Meets Affordability”

Services Offered:
Procurement
Fabrication
Distribution
Logistics
Import/Export

Requirements
Must have
• Nice quality double sided Business Card design, Letterhead design needs to be A4
Nice to have
• possible ideas on tag lines

```html
<!DOCTYPE html>
<html lang="en">
<head>
<meta charset="utf-8">
<title>Vantorra Stationery</title>
<link href="https://fonts.googleapis.com/css2?family=Mulish:wght@400;600;800&display=swap" rel="stylesheet">
<style>
:root{
  --stage:#b3b3b3;
  --charcoal:#333333;
  --red:#ee3537;
  --white:#ffffff;
  --light:#e6e6e6;
  --paper-end:#efefef;
}
*{margin:0;padding:0;box-sizing:border-box}
html,body{width:1200px;height:911px;overflow:hidden}
body{background:var(--stage);font-family:"Mulish",sans-serif;color:var(--white);position:relative}
.icon{width:6px;height:6px;fill:var(--red);flex:none}
.contact-line{display:flex;align-items:center;gap:4px;white-space:nowrap}
.brand-name{font-family:"Mulish",sans-serif;font-weight:800;color:var(--red);letter-spacing:.5px;display:flex;align-items:center;gap:5px;text-transform:uppercase}
.brand-square{background:var(--red);flex:none}

/* letterhead */
.letterhead{position:absolute;left:33px;top:61px;width:565px;height:794px;background:linear-gradient(160deg,var(--white) 35%,var(--paper-end) 100%)}
.letterhead-header{height:118px;background:var(--charcoal);border-bottom:7px solid var(--red);position:relative}
.letterhead .brand-name{position:absolute;left:45px;top:80px;font-size:21px}
.letterhead .brand-square{width:14px;height:14px}
.letterhead-contact{position:absolute;left:401px;top:45px;font-size:7.6px;line-height:10.6px}
.letterhead-contact .gap{height:9px}

/* cards */
.card{position:absolute;width:238px;height:136px;border-radius:6px;background:var(--charcoal)}
.card-front{left:641px;top:206px;border:1px solid #222}
.card-front .brand-name{position:absolute;left:15px;top:80px;font-size:13px}
.card-front .brand-square{width:9px;height:9px}
.card-divider{position:absolute;left:115px;top:35px;width:1px;height:66px;background:var(--light)}
.card-front .details{position:absolute;left:124px;top:33px;font-size:5.2px;line-height:7.6px}
.card-front .person{color:var(--red);font-size:7.2px;font-weight:600}
.card-front .gap{height:6px}
.card-back{left:893px;top:206px;display:flex;align-items:center;justify-content:center}
.card-back .brand-name{font-size:16px}
.card-back .brand-square{width:11px;height:11px}
.card-red{left:641px;top:379px;background:var(--red);display:flex;align-items:center;justify-content:center}
.card-red .brand-name{color:var(--white);font-size:16px}
.card-red .brand-square{background:var(--white);width:11px;height:11px}
.card-pattern{left:893px;top:379px;background:linear-gradient(135deg,#4a4a4a 0%,#2e2e2e 55%,#151515 100%)}

/* email signature */
.signature{position:absolute;left:637px;top:550px;width:499px;height:128px;background:var(--charcoal);border:1px solid #222}
.signature-accent{position:absolute;left:0;top:29px;width:5px;height:26px;background:var(--red)}
.signature-person{position:absolute;left:25px;top:30px}
.signature-person .person{color:var(--red);font-size:11.5px;font-weight:600;line-height:14px}
.signature-person .role{font-size:8.6px;line-height:13px}
.signature-divider{position:absolute;left:158px;top:32px;width:1px;height:63px;background:var(--light)}
.signature-contact{position:absolute;left:175px;top:30px;font-size:8.4px;line-height:11.4px}
.signature-contact .gap{height:10px}
.signature .icon{width:7px;height:7px}
.signature .brand-name{position:absolute;left:358px;top:77px;font-size:18px}
.signature .brand-square{width:12px;height:12px}
</style>
</head>
<body>

<svg width="0" height="0" style="position:absolute">
  <symbol id="icon-phone" viewBox="0 0 10 10"><path d="M2 0.5l1.8 2-1 1.2c.6 1.3 1.4 2.1 2.6 2.6l1.2-1 2 1.8-1 1.8C5 8.7 1.3 5 .4 1.5z"/></symbol>
  <symbol id="icon-mail" viewBox="0 0 10 10"><path d="M0 2h10v6H0z M0 2l5 3.2L10 2" /></symbol>
  <symbol id="icon-globe" viewBox="0 0 10 10"><path fill="none" stroke="#ee3537" stroke-width="1" d="M5 .6a4.4 4.4 0 1 0 0 8.8a4.4 4.4 0 1 0 0-8.8zM.6 5h8.8M5 .6c-2.2 2.4-2.2 6.4 0 8.8M5 .6c2.2 2.4 2.2 6.4 0 8.8"/></symbol>
</svg>

<section class="letterhead">
  <header class="letterhead-header">
    <div class="brand-name"><span class="brand-square"></span>Vantorra</div>
    <div class="letterhead-contact">
      <div>412 Harbor Street</div>
      <div>Suite 208, Oakdale, CA 90217</div>
      <div class="gap"></div>
      <div class="contact-line"><svg class="icon"><use href="#icon-phone"/></svg>555-014-2738</div>
      <div class="contact-line"><svg class="icon"><use href="#icon-mail"/></svg>daniel.moreau@vantorra-example.com</div>
      <div class="contact-line"><svg class="icon"><use href="#icon-globe"/></svg>vantorra-example.com</div>
    </div>
  </header>
</section>

<section class="card card-front">
  <div class="brand-name"><span class="brand-square"></span>Vantorra</div>
  <div class="card-divider"></div>
  <div class="details">
    <div class="person">DANIEL MOREAU</div>
    <div>Development Manager Officer</div>
    <div class="gap"></div>
    <div>412 Harbor Street</div>
    <div>Suite 208, Oakdale, CA 90217</div>
    <div class="gap"></div>
    <div class="contact-line"><svg class="icon" style="width:4px;height:4px"><use href="#icon-phone"/></svg>555-014-2738</div>
    <div class="contact-line"><svg class="icon" style="width:4px;height:4px"><use href="#icon-mail"/></svg>daniel.moreau@vantorra-example.com</div>
    <div class="contact-line"><svg class="icon" style="width:4px;height:4px"><use href="#icon-globe"/></svg>vantorra-example.com</div>
  </div>
</section>

<section class="card card-back">
  <div class="brand-name"><span class="brand-square"></span>Vantorra</div>
</section>

<section class="card card-red">
  <div class="brand-name"><span class="brand-square"></span>Vantorra</div>
</section>

<section class="card card-pattern" role="img" aria-label="Dark card back with a repeating tonal brand pattern fading from grey to black"></section>

<section class="signature">
  <div class="signature-accent"></div>
  <div class="signature-person">
    <div class="person">DANIEL MOREAU</div>
    <div class="role">Development Manager Officer</div>
  </div>
  <div class="signature-divider"></div>
  <div class="signature-contact">
    <div>412 Harbor Street</div>
    <div>Suite 208, Oakdale, CA 90217</div>
    <div class="gap"></div>
    <div class="contact-line"><svg class="icon"><use href="#icon-phone"/></svg>555-014-2738</div>
    <div class="contact-line"><svg class="icon"><use href="#icon-mail"/></svg>daniel.moreau@vantorra-example.com</div>
    <div class="contact-line"><svg class="icon"><use href="#icon-globe"/></svg>vantorra-example.com</div>
  </div>
  <div class="brand-name"><span class="brand-square"></span>Vantorra</div>
</section>

</body>
</html>
```